Website design project for ICT Business - Bright Harbour Tx

We need website built for our new startup. The company name is Bright Harbour TX. Bright Harbour is an Information Communication Technology business that aims to help small to medium businesses unlock the power and benefits of the cloud. We are a sales and support business that consults with our clients to assist them in migrating to the cloud safely and without business interruption.

Coding

Coded - Design and coding required

Number of Pages Required

4 page

```html
<!DOCTYPE html>
<html lang="en">
<head>
<meta charset="utf-8">
<title>Bright Harbour TX</title>
<link href="https://fonts.googleapis.com/css2?family=Exo+2:wght@300;400;600;800&family=Open+Sans:wght@400;600;700&display=swap" rel="stylesheet">
<style>
:root{
  --sky:#1ba9e6;
  --sky-light:#2fb8f0;
  --sky-deep:#0c78bf;
  --navy:#0b4a88;
  --night:#0f1d2a;
  --ink:#333;
  --muted:#6a6a6a;
  --field:#efefef;
  --white:#fff;
  --head:"Exo 2",sans-serif;
  --body:"Open Sans",sans-serif;
}
*{margin:0;padding:0;box-sizing:border-box}
html,body{width:1200px;height:3448px;overflow:hidden}
body{position:relative;font-family:var(--body);color:var(--ink);background:var(--white)}
.abs{position:absolute}
a{color:inherit;text-decoration:none}
h1,h2,h3,h4{font-weight:400}

/* header */
.site-header{left:0;top:0;width:1200px;height:126px;background:var(--white);z-index:2}
.brand{left:80px;top:50px;font-family:var(--head);font-weight:600;font-size:34px;color:var(--sky-deep);display:flex;align-items:center;gap:12px}
.brand-dot{width:34px;height:34px;border-radius:50%;background:var(--sky)}
.top-phone{left:790px;top:8px;font-size:20px;font-weight:600;color:var(--navy);display:flex;align-items:center;gap:10px}
.top-social{top:12px;width:18px;height:18px;border-radius:50%;background:#9aa7b2}
.main-nav{left:444px;top:64px;display:flex;font-size:18px;text-transform:uppercase;color:#444}
.main-nav a{height:42px;line-height:42px;padding:0 20px;margin-right:30px}
.main-nav a.active{background:var(--sky);color:var(--white)}

/* hero + welcome */
.hero-art{left:0;top:126px}
.hero-title{left:80px;top:244px;font-family:var(--head);font-weight:800;font-size:54px;line-height:62px;color:var(--white);letter-spacing:2px}
.hero-sub{left:80px;top:380px;font-size:22px;color:var(--white)}
.pill{border-radius:26px;font-weight:700;text-transform:uppercase;display:flex;align-items:center;justify-content:center}
.hero-cta{left:80px;top:441px;width:198px;height:51px;background:var(--sky);color:var(--white);font-size:16px}
.welcome-title{left:80px;top:800px;font-family:var(--head);font-weight:300;font-size:46px;line-height:52px;color:var(--white)}
.welcome-text{left:80px;top:925px;width:575px;font-size:15px;line-height:23px;color:var(--white)}
.read-more{left:78px;top:1023px;width:170px;height:49px;background:var(--white);color:var(--sky);font-size:16px}
.welcome-art{left:667px;top:747px;width:470px;height:322px;border-radius:60px;background:radial-gradient(ellipse at 50% 55%,#ffffff 0%,#d9f1fd 45%,#7fd0f5 100%)}

/* services */
.services{left:0;top:1120px;width:1200px;height:738px;background:radial-gradient(ellipse at 60% 40%,#1a6fb5 0%,var(--navy) 60%,#083a6e 100%)}
.section-title{width:1200px;left:0;text-align:center;font-family:var(--head);font-weight:400;font-size:44px;letter-spacing:1px}
.services .section-title{top:48px;color:var(--white)}
.services-intro{left:0;top:118px;width:1200px;text-align:center;font-size:15px;line-height:23px;color:var(--white)}
.services-art{left:97px;top:213px;width:455px;height:437px;border-radius:40px;background:radial-gradient(ellipse at 40% 35%,#7fe0ff 0%,#2aa7e8 40%,rgba(20,110,190,.2) 100%)}
.service{left:593px;width:520px;height:120px;color:var(--white)}
.service-icon{left:0;top:0;width:115px;height:115px;border-radius:50%;border:7px solid var(--white);background:#3a86c4}
.service-name{left:143px;top:-6px;font-family:var(--head);font-weight:400;font-size:27px}
.service-text{left:143px;top:32px;width:340px;font-size:15px;line-height:23px}

/* quote */
.quote-title{top:1900px;color:var(--navy)}
.accent{color:var(--sky)}
.field{background:var(--field);font-size:14px;color:#999;padding:14px 22px}
.field.outlined{background:var(--white);border:2px solid #ddd}
.submit{left:460px;top:2124px;width:623px;height:51px;background:var(--sky);color:var(--white);font-size:22px;letter-spacing:1px;display:flex;align-items:center;justify-content:center}

/* testimonial */
.testimonial{left:0;top:2226px;width:1200px;height:414px;background:linear-gradient(180deg,#27aae6,#1596d6)}
.testimonial .section-title{top:54px;color:var(--white)}
.quote-mark{left:576px;top:120px;width:48px;height:48px;border:3px solid var(--white);border-radius:50%;color:var(--white);font-family:Georgia,serif;font-size:44px;line-height:62px;text-align:center}
.testimonial-text{left:156px;top:192px;width:888px;text-align:center;font-size:15px;line-height:26px;color:var(--white)}
.arrow{top:198px;width:32px;height:32px;border:2px solid var(--white);border-radius:50%}
.avatar{left:487px;top:274px;width:80px;height:80px;border-radius:50%;border:3px solid var(--white);background:#d8c7b8}
.client-name{left:593px;top:302px;font-size:18px;color:var(--white);text-transform:uppercase}

/* news */
.news-title{top:2680px;color:var(--navy)}
.news-item{z-index:2}
.news-photo{width:207px;height:141px;background:linear-gradient(135deg,#c7d6e2,#6f8aa3)}
.news-head{font-family:var(--body);font-weight:400;font-size:15px;color:var(--sky-deep)}
.news-date{font-size:14px;color:#555}
.news-text{width:260px;font-size:15px;line-height:24px;color:var(--muted)}

/* footer */
.footer-art{left:0;top:2870px}
.footer-brand{left:80px;top:3215px;font-family:var(--head);font-weight:600;font-size:34px;color:var(--sky)}
.footer-social{top:3316px;width:46px;height:46px;border-radius:50%;background:var(--white)}
.footer-social.first{background:var(--sky)}
.footer-heading{top:3176px;font-family:var(--head);font-weight:400;font-size:21px;color:var(--white);letter-spacing:.5px}
.footer-links{left:350px;top:3222px;font-size:15px;line-height:34px;color:var(--white);list-style:none}
.footer-input{left:621px;width:232px;height:40px;border:1px solid #9aa;color:var(--white);font-size:14px;padding:9px 6px}
.subscribe{left:621px;top:3329px;width:150px;height:41px;background:var(--white);color:var(--navy);font-size:17px;display:flex;align-items:center;justify-content:center;text-transform:uppercase}
.contact-item{left:890px;font-size:15px;line-height:24px;color:var(--white);display:flex;gap:12px;width:260px}
.contact-item svg{flex:none;margin-top:4px}
.copyright{left:0;top:3398px;width:1200px;height:50px;background:var(--sky);color:var(--white);font-size:15px;display:flex;align-items:center;justify-content:center}
</style>
</head>
<body>

<header class="site-header abs">
  <div class="brand abs"><span class="brand-dot"></span>Bright Harbour</div>
  <div class="top-phone abs">
    <svg width="18" height="18" viewBox="0 0 24 24"><path fill="#0b4a88" d="M6.6 10.8a15.1 15.1 0 0 0 6.6 6.6l2.2-2.2c.3-.3.7-.4 1-.2 1.1.4 2.3.6 3.6.6.6 0 1 .4 1 1V20c0 .6-.4 1-1 1C10.6 21 3 13.4 3 4c0-.6.4-1 1-1h3.5c.6 0 1 .4 1 1 0 1.3.2 2.5.6 3.6.1.3 0 .7-.2 1z"/></svg>
    (123) 456-7890
  </div>
  <span class="top-social abs" style="left:1030px"></span>
  <span class="top-social abs" style="left:1069px"></span>
  <span class="top-social abs" style="left:1108px"></span>
  <nav class="main-nav abs">
    <a class="active" href="#">Home</a>
    <a href="#">About Us</a>
    <a href="#">Services</a>
    <a href="#">News</a>
    <a href="#">Contact Us</a>
  </nav>
</header>

<svg class="hero-art abs" width="1200" height="994" viewBox="0 126 1200 994">
  <defs>
    <linearGradient id="heroShade" x1="0" y1="0" x2="1" y2="0">
      <stop offset="0" stop-color="#0a1826"/>
      <stop offset=".5" stop-color="#123a5e"/>
      <stop offset=".8" stop-color="#2a6ea6"/>
      <stop offset="1" stop-color="#14304c"/>
    </linearGradient>
  </defs>
  <rect x="0" y="126" width="1200" height="640" fill="url(#heroShade)" role="img" aria-label="Photo of a businessman touching a network of cloud service icons"/>
  <polygon points="0,550 700,718 1200,515 1200,1120 0,1120" fill="#0c5fa3"/>
  <polygon points="0,568 700,745 1200,540 1200,1120 0,1120" fill="var(--sky)"/>
</svg>

<h1 class="hero-title abs">BRIGHT<br>HARBOUR TX</h1>
<p class="hero-sub abs">Lorem Ipsum is simply dummy</p>
<a class="hero-cta pill abs" href="#">Contact us now</a>

<h2 class="welcome-title abs">WELCOME TO<br>BRIGHT HARBOUR TX</h2>
<p class="welcome-text abs">Lorem Ipsum is simply dummy text of the printing and typesetting industry. Lorem Ipsum has been the industry's standard dummy text ever since the 1500s, when an unknown printer took a galley of type and scrambled it to...</p>
<a class="read-more pill abs" href="#">Read more &raquo;</a>
<div class="welcome-art abs" role="img" aria-label="Illustration of a laptop resting on glossy clouds"></div>

<section class="services abs">
  <h2 class="section-title abs">OUR SERVICES</h2>
  <p class="services-intro abs">Lorem Ipsum is simply dummy text of the printing and typesetting industry.<br>Lorem Ipsum has a been the industry's standard.</p>
  <div class="services-art abs" role="img" aria-label="Illustration of a cloud joined to circuit lines"></div>

  <div class="service abs" style="top:221px">
    <div class="service-icon abs" role="img" aria-label="ICT projects icon"></div>
    <h3 class="service-name abs">ICT Projects</h3>
    <p class="service-text abs">Lorem Ipsum is simply dummy text of the printing and typesetting industry. Lorem Ipsum has been the industry's standard dummy text.</p>
  </div>
  <div class="service abs" style="top:377px">
    <div class="service-icon abs" role="img" aria-label="ICT architecture icon"></div>
    <h3 class="service-name abs">ICT Architecture</h3>
    <p class="service-text abs">Lorem Ipsum is simply dummy text of the printing and typesetting industry. Lorem Ipsum has been the industry's standard dummy text.</p>
  </div>
  <div class="service abs" style="top:536px">
    <div class="service-icon abs" role="img" aria-label="Cloud consultation icon"></div>
    <h3 class="service-name abs">Cloud consultation</h3>
    <p class="service-text abs">Lorem Ipsum is simply dummy text of the printing and typesetting industry. Lorem Ipsum has been the industry's standard dummy text.</p>
  </div>
</section>

<h2 class="section-title quote-title abs">GET A <span class="accent">FREE QUOTE</span></h2>
<div class="field outlined abs" style="left:115px;top:1998px;width:333px;height:53px">Name</div>
<div class="field abs" style="left:115px;top:2060px;width:333px;height:53px">E - Mail</div>
<div class="field abs" style="left:115px;top:2122px;width:333px;height:53px">Phone</div>
<div class="field abs" style="left:460px;top:1998px;width:623px;height:115px">Message</div>
<div class="submit abs">SUBMIT</div>

<section class="testimonial abs" role="img" aria-label="Blue tinted photo of a team meeting in an office">
  <h2 class="section-title abs">WHAT OUR CLIENT SAY</h2>
  <div class="quote-mark abs">&ldquo;</div>
  <p class="testimonial-text abs">Lorem Ipsum is simply dummy text of the printing and typesetting industry. Lorem Ipsum has been the industry's standard dummy text ever since the 1500s, when an unknown printer took a galley of type and scrambled it to make a type specimen book. It has survived not only five centuries, but also the leap into electronic type setting.</p>
  <svg class="arrow abs" style="left:81px" viewBox="0 0 32 32"><path d="M18 10l-6 6 6 6" fill="none" stroke="#fff" stroke-width="2"/></svg>
  <svg class="arrow abs" style="left:1092px" viewBox="0 0 32 32"><path d="M14 10l6 6-6 6" fill="none" stroke="#fff" stroke-width="2"/></svg>
  <div class="avatar abs" role="img" aria-label="Client portrait"></div>
  <p class="client-name abs">- Client Name</p>
</section>

<svg class="footer-art abs" width="1200" height="528" viewBox="0 2870 1200 528">
  <rect x="0" y="2870" width="1200" height="528" fill="var(--white)"/>
  <polygon points="0,2930 700,3130 1200,2892 1200,3398 0,3398" fill="var(--sky)"/>
  <polygon points="0,2950 700,3158 1200,2912 1200,3398 0,3398" fill="var(--night)"/>
</svg>

<h2 class="section-title news-title abs">RECENT <span class="accent">NEWS</span></h2>
<article class="news-item">
  <div class="news-photo abs" style="left:78px;top:2779px" role="img" aria-label="Photo of business partners shaking hands"></div>
  <h3 class="news-head abs" style="left:320px;top:2778px">Lorem Ipsum is simply dummy</h3>
  <p class="news-date abs" style="left:320px;top:2803px">&#9638; Decvember 23, 2016</p>
  <p class="news-text abs" style="left:320px;top:2833px">Lorem Ipsum is simply dummy text of the printing and typesetting industry.</p>
</article>
<article class="news-item">
  <div class="news-photo abs" style="left:625px;top:2779px" role="img" aria-label="Photo of a desk with laptop and office items"></div>
  <h3 class="news-head abs" style="left:864px;top:2778px">Lorem Ipsum is simply dummy</h3>
  <p class="news-date abs" style="left:864px;top:2803px">&#9638; December 23, 2016</p>
  <p class="news-text abs" style="left:864px;top:2833px">Lorem Ipsum is simply dummy text of the printing and typesetting industry.</p>
</article>

<div class="footer-brand abs">Bright Harbour</div>
<span class="footer-social first abs" style="left:80px"></span>
<span class="footer-social abs" style="left:154px"></span>
<span class="footer-social abs" style="left:228px"></span>

<h4 class="footer-heading abs" style="left:350px">Useful Links</h4>
<ul class="footer-links abs">
  <li>Home</li><li>About Us</li><li>Services</li><li>News</li><li>Contact Us</li>
</ul>

<h4 class="footer-heading abs" style="left:621px">Newsletter</h4>
<div class="footer-input abs" style="top:3223px">Enter Name</div>
<div class="footer-input abs" style="top:3276px">Enter Email</div>
<div class="subscribe abs">Subscribe</div>

<h4 class="footer-heading abs" style="left:890px">Get In Touch With Us</h4>
<div class="contact-item abs" style="top:3224px">
  <svg width="14" height="18" viewBox="0 0 14 18"><path d="M7 0a7 7 0 0 0-7 7c0 5 7 11 7 11s7-6 7-11a7 7 0 0 0-7-7zm0 9.5A2.5 2.5 0 1 1 7 4.5a2.5 2.5 0 0 1 0 5z" fill="#fff"/></svg>
  <span>Lorem Ipsum is simply dummy text of the printing and typesetting industry.</span>
</div>
<div class="contact-item abs" style="top:3310px">
  <svg width="16" height="16" viewBox="0 0 24 24"><path fill="#fff" d="M6.6 10.8a15.1 15.1 0 0 0 6.6 6.6l2.2-2.2c.3-.3.7-.4 1-.2 1.1.4 2.3.6 3.6.6.6 0 1 .4 1 1V20c0 .6-.4 1-1 1C10.6 21 3 13.4 3 4c0-.6.4-1 1-1h3.5c.6 0 1 .4 1 1 0 1.3.2 2.5.6 3.6.1.3 0 .7-.2 1z"/></svg>
  <span>123 456 7890</span>
</div>
<div class="contact-item abs" style="top:3348px">
  <svg width="18" height="14" viewBox="0 0 18 14"><rect x="1" y="1" width="16" height="12" fill="none" stroke="#fff" stroke-width="1.6"/><path d="M1 1l8 6 8-6" fill="none" stroke="#fff" stroke-width="1.6"/></svg>
  <span>Lorem Ipsum is simply</span>
</div>

<footer class="copyright abs">&copy;&nbsp;<strong>BRIGHT HARBOUR TX</strong>&nbsp;- 2016. All Rights Reserved.</footer>

</body>
</html>
```